Captain Pebble - Book cover for a children's book

I need a book cover for a children's book size A 4 which can be used for print and ebook. The story has about 16,000 words and ten hand-made watercolor illustrations. One of these should be on the book cover (file provided). The design of the book cover should match the illustration.
The book is for children aged 6-10 years old.

Name of the book: Captain Pebble
written by: Tilda Vorhagen
illustrated by: Celeste Marina Dunn

Thank you!

Synopsis:
Captain Pebble is the story of a frustrated mouse who is the leader of a questing team, comprised of himself, a racoon, a slug, and a giraffe – Captain Pebble (ambitious, but with low self-esteem that he covers up by being bossy), Pippa Parrot (beautiful, forgetful, and unable to read), Wendy Worm (confident and strong, but extremely slow) and Oliver Otter (jolly and practical, yet single-mindedly focused on food). One of the many running jokes throughout the book is that Captain Pebble thinks Oliver is a pig, a confusion which is only resolved near the end of the book. Captain Pebble sees himself as the rightful leader of the team, as he is by far the smartest. He also fears he will not be successful in completing his quest, as he has been forced to team up with less than ideal quest teammates. During the team’s quest, Captain Pebble loses each of his team members, one by one. Following the revelation of her illiteracy, Pippa opts to stay behind at the first obstacle, Oliver runs off after apples for lunch, and Wendy gets distracted. Captain Pebble is excited to be able to go off on his own but gets snatched by an eagle. The other three team members band together to rescue Captain Pebble in haphazard circumstances. They all return to Quest school jubilant and ready to receive their diplomas, not realising that Captain Pebble will not qualify because he was the one who had to be rescued. When Captain Pebble does not get his diploma, the team come together and recall that during the rescue Captain Pebble had in fact also saved Wendy Worm, allowing them all to graduate together.
With so many different characteristics, the team show that they are stronger together than as individuals. By embracing their weaknesses and vulnerabilities they learn to cooperate and in the end this helps them to succeed. The team agree to stick together for future adventures.

Target Market(s)

Children 6-10 years old + their carers/grand-parents/ primary school teachers

Font styles to use
Serif
Sans Serif

Requirements
Must have
• Beautiful colors (matching the provided illustration), must have the provided illustration on the cover, must be appealing and heart-warming, spiking curiosity.

Must feature book name, name of author and name of illustrator.

Text for blurb on the back of the book cover:

"Captain Pebble tells the delightful story of four animals on a quest. These four could not be more different – there is a mouse, a giraffe, a slug, and a pig. But wait – is this really true? Captain Pebble, who thinks he is the leader, seems to have missed his zoology lessons at school.
There is more than one team competing to complete the quest. Can our odd team beat the lions? Who will be faster? Does being faster mean that you win? Find out what really matters in the end!"
Should not have
• should not be over-loaded, no large white spaces

```html
<!DOCTYPE html>
<html lang="en">
<head>
<meta charset="utf-8">
<title>Captain Pebble – Book Cover</title>
<link href="https://fonts.googleapis.com/css2?family=Fredoka:wght@400;500;600&family=Patrick+Hand&family=Special+Elite&display=swap" rel="stylesheet">
<style>
  :root {
    --sky-blue: #3fb3e6;
    --deep-blue: #2a8fd8;
    --lilac: #b58ad0;
    --rose: #e98ab4;
    --sun-yellow: #f6e59a;
    --cream: #fbf1c8;
    --grass: #8cc260;
    --grass-dark: #5f9a3e;
    --giraffe-orange: #e98a3a;
    --giraffe-gold: #f4b94a;
    --mouse-grey: #6f6c78;
    --title-orange: #f26a14;
    --navy: #123a6b;
    --ink: #1c1c1c;
    --credit-red: #7a1c12;
    --white: #ffffff;
  }
  * { margin: 0; padding: 0; box-sizing: border-box; }
  html, body { width: 1200px; height: 848px; overflow: hidden; background: #fff; }
  .cover {
    position: relative;
    width: 1200px;
    height: 848px;
    overflow: hidden;
  }
  .cover__painting {
    position: absolute; inset: 0;
    background:
      radial-gradient(ellipse 380px 300px at 430px 90px, rgba(233,138,180,.75), transparent 70%),
      radial-gradient(ellipse 300px 260px at 1150px 80px, rgba(63,179,230,.7), transparent 70%),
      radial-gradient(ellipse 420px 320px at 1000px 560px, rgba(246,229,154,.95), transparent 75%),
      radial-gradient(ellipse 260px 260px at 640px 300px, rgba(181,138,208,.7), transparent 70%),
      linear-gradient(100deg, var(--sky-blue) 0%, var(--deep-blue) 28%, #79c6ea 48%, var(--cream) 78%, var(--sun-yellow) 100%);
  }
  .cover__meadow {
    position: absolute; left: 0; right: 0; bottom: 0; height: 150px;
    background: linear-gradient(180deg, rgba(140,194,96,0) 0%, rgba(140,194,96,.75) 40%, var(--grass) 70%, var(--grass-dark) 100%);
  }
  .cover__giraffe {
    position: absolute; left: 640px; top: -10px; width: 370px; height: 480px;
    border-radius: 45% 45% 50% 50% / 40% 40% 60% 60%;
    background: radial-gradient(ellipse at 50% 45%, var(--giraffe-orange) 0%, var(--giraffe-gold) 55%, rgba(244,185,74,0) 75%);
  }
  .cover__mouse {
    position: absolute; width: 100px; height: 160px; border-radius: 40% 40% 30% 30%;
    background: radial-gradient(ellipse at 50% 50%, var(--mouse-grey) 0%, rgba(111,108,120,.5) 50%, rgba(111,108,120,0) 75%);
  }
  .cover__mouse--back { left: 36px; top: 684px; }
  .cover__mouse--front { left: 1010px; top: 684px; }

  .title, .author {
    font-family: "Fredoka", system-ui, sans-serif;
    position: absolute; white-space: nowrap; line-height: 1;
  }
  .title { font-weight: 500; }
  .author { font-weight: 400; }

  .back__title { left: 58px; top: 118px; font-size: 62px; color: var(--white); }
  .back__author { right: 668px; top: 204px; font-size: 34px; color: var(--white); }
  .back__blurb {
    position: absolute; left: 50px; top: 350px; width: 500px;
    font-family: "Patrick Hand", "Comic Sans MS", cursive;
    font-size: 16px; line-height: 27.4px; text-transform: uppercase;
    text-align: center; color: var(--ink);
  }
  .back__blurb p + p { margin-top: 27px; }

  .spine__title, .spine__author {
    position: absolute; writing-mode: vertical-rl; color: var(--white);
  }
  .spine__title { left: 574px; top: 60px; font-size: 34px; }
  .spine__author { left: 580px; top: 552px; font-size: 26px; }

  .front__title { right: 46px; top: 494px; font-size: 66px; color: var(--title-orange); }
  .front__author { right: 46px; top: 578px; font-size: 36px; color: var(--navy); }
  .front__credit {
    position: absolute; left: 700px; width: 260px; top: 744px;
    font-family: "Special Elite", "Courier New", monospace;
    font-size: 19px; line-height: 27px; text-align: center; color: var(--credit-red);
  }
</style>
</head>
<body>
<main class="cover">
  <div class="cover__painting" role="img" aria-label="Watercolour wash in sky blue, lilac, pink and warm yellow spanning the whole cover"></div>
  <div class="cover__meadow" role="img" aria-label="Watercolour meadow of grass and small flowers along the bottom edge"></div>
  <div class="cover__giraffe" role="img" aria-label="Watercolour illustration of a giraffe's head looking down"></div>
  <div class="cover__mouse cover__mouse--back" role="img" aria-label="Illustration of a small mouse standing in the grass"></div>
  <div class="cover__mouse cover__mouse--front" role="img" aria-label="Illustration of a small mouse standing in the grass"></div>

  <section class="back">
    <h2 class="title back__title">Captain Pebble</h2>
    <p class="author back__author">Tilda Vorhagen</p>
    <div class="back__blurb">
      <p>"Captain Pebble tells the delightful story of four animals on a quest. These four could not be more different – there is a mouse, a giraffe, a slug, and a pig. But wait – is this really true? Captain Pebble, who thinks he is the leader, seems to have missed his zoology lessons at school.</p>
      <p>There is more than one team competing to complete the quest. Can our odd team beat the lions? Who will be faster? Does being faster mean that you win? Find out what really matters in the end!"</p>
    </div>
  </section>

  <section class="spine">
    <p class="title spine__title">Captain Pebble</p>
    <p class="author spine__author">Tilda Vorhagen</p>
  </section>

  <section class="front">
    <h1 class="title front__title">Captain Pebble</h1>
    <p class="author front__author">Tilda Vorhagen</p>
    <p class="front__credit">illustrated by<br>Celeste Marina Dunn</p>
  </section>
</main>
</body>
</html>
```